5 Blog Posts and Lead Magnet Needs Branding for Remodeling Company

I have 5 blogs and a website lead magnet that have content written but need some design and layout help to align with my brand identity. The content will need to be formatted for social media and website. I have a logo, colors and font. I also have a website I'm pretty happy with right now that can provide direction.
Target Market(s)
Age 40-65, Average salary 250K, Male/Female Professional College + Married 3 + Mid-full size car with high end finishes.
Industry/Entity Type
Construction, remodeling
Colors
Designer to choose colors to be used in the design.
Look and feel

```html
<!DOCTYPE html>
<html lang="en">
<head>
<meta charset="UTF-8">
<title>5 Mistakes When Planning a Major Home Remodel</title>
<link rel="stylesheet" href="https://fonts.googleapis.com/css2?family=Montserrat:wght@500;700;800;900&display=swap">
<style>
  :root {
    --paper: #f4f5f7;
    --navy: #0f1d4a;
    --green: #86a337;
    --white: #ffffff;
  }
  * { margin: 0; padding: 0; box-sizing: border-box; }
  html, body {
    width: 848px;
    height: 1200px;
    overflow: hidden;
    background: var(--paper);
  }
  .cover {
    position: relative;
    width: 848px;
    height: 1200px;
    background: var(--paper);
    font-family: "Montserrat", Arial, sans-serif;
    color: var(--navy);
  }
  .brand {
    position: absolute;
    left: 58px;
    top: 78px;
    width: 160px;
    font-weight: 800;
    font-size: 20px;
    line-height: 1.1;
    color: var(--navy);
    letter-spacing: 0.2px;
  }
  .brand-name { display: block; font-size: 30px; }
  .hero-photo {
    position: absolute;
    left: 433px;
    top: 72px;
    width: 342px;
    height: 1055px;
    background:
      linear-gradient(180deg, #eef0f1 0%, #e3e5e6 30%, #c9ccd0 45%, #8fa6c6 62%, #7f95b3 78%, #9fb0c4 92%, #d9dbdd 100%);
  }
  .headline {
    position: absolute;
    left: 0;
    top: 0;
    width: 848px;
    height: 1200px;
    pointer-events: none;
  }
  .big-number { font-weight: 900; fill: var(--green); }
  .title-main { font-weight: 900; fill: var(--navy); }
  .title-sub { font-weight: 500; fill: var(--navy); }
  .title-strong { font-weight: 800; fill: var(--navy); }
  .tagline-band { fill: var(--green); }
  .tagline-text { font-weight: 800; fill: var(--white); }
</style>
</head>
<body>
  <main class="cover">
    <div class="brand">
      <span class="brand-name">Larkin</span>
      Home Improvements
    </div>

    <div class="hero-photo" role="img" aria-label="Smiling couple in a bright white kitchen looking at a laptop together, the man holding a dark mug"></div>

    <svg class="headline" viewBox="0 0 848 1200" width="848" height="1200" aria-label="5 mistakes people make when planning a major home remodel, and how to avoid them">
      <text class="big-number" x="60" y="874" font-size="535" textLength="314" lengthAdjust="spacingAndGlyphs">5</text>
      <text class="title-main" x="60" y="929" font-size="58" textLength="310" lengthAdjust="spacingAndGlyphs">MISTAKES</text>
      <text class="title-sub" x="62" y="985" font-size="30" textLength="312" lengthAdjust="spacing">PEOPLE MAKE WHEN</text>
      <text class="title-sub" x="62" y="1013" font-size="30" textLength="312" lengthAdjust="spacing">PLANNING A MAJOR</text>
      <text class="title-strong" x="62" y="1045" font-size="39" textLength="313" lengthAdjust="spacingAndGlyphs">HOME REMODEL</text>
      <rect class="tagline-band" x="0" y="1073" width="374" height="55"></rect>
      <text class="tagline-text" x="60" y="1108" font-size="23" textLength="297" lengthAdjust="spacingAndGlyphs">AND HOW TO AVOID THEM</text>
    </svg>
  </main>
</body>
</html>
```